Labor Day Sale Website Banner For High End Jewelry Website

We need a banner for our website (fernlite.com) for a Labor Day Sale. The banner should be a size 1187 × 400. I have included a few pieces of jewelry to be included in the banner (do not need to use all, can use just some). The banner should say:
"Labor Day Sale"
"Save 15% on Everything!"
Use Promo Code: BLOSSOM

Target Market(s)

Affluent Female Consumers

Industry/Entity Type

Jewelry

Colors

Designer to choose colors to be used in the design.

```html
<!DOCTYPE html>
<html lang="en">
<head>
<meta charset="utf-8">
<title>Labor Day Sale Banner</title>
<link rel="stylesheet" href="https://fonts.googleapis.com/css2?family=Raleway:wght@500;600;700&family=Great+Vibes&display=swap">
<style>
  :root {
    --salmon: #e8826f;
    --ink: #1f1f1f;
    --cream: #fdf1d6;
    --gold: #d9a82e;
    --gold-light: #f3d57a;
    --gem-blue: #6b6fb8;
    --gem-pink: #c8558f;
  }
  html, body {
    margin: 0;
    padding: 0;
    width: 1200px;
    height: 404px;
    overflow: hidden;
    background: #ffffff;
  }
  .banner {
    position: relative;
    width: 1200px;
    height: 404px;
    overflow: hidden;
    background: var(--cream);
    font-family: "Raleway", Arial, sans-serif;
  }
  .banner__backdrop {
    position: absolute;
    inset: 0;
  }
  .headline {
    margin: 0;
    color: var(--salmon);
    font-weight: 600;
  }
  .headline__labor,
  .headline__day {
    position: absolute;
    left: 66px;
    line-height: 1;
    white-space: nowrap;
  }
  .headline__labor {
    top: 50px;
    font-size: 80px;
    letter-spacing: 5px;
  }
  .headline__day {
    top: 110px;
    font-size: 136px;
    letter-spacing: 9px;
  }
  .headline__rule {
    position: absolute;
    left: 62px;
    top: 257px;
    width: 304px;
    height: 2px;
    margin: 0;
    border: 0;
    background: var(--salmon);
  }
  .offer {
    position: absolute;
    left: 62px;
    top: 264px;
    width: 304px;
    text-align: center;
    color: var(--ink);
  }
  .offer__savings {
    margin: 0;
    font-size: 19px;
    font-weight: 500;
    line-height: 26px;
  }
  .offer__savings strong {
    color: var(--salmon);
    font-weight: 700;
  }
  .offer__code {
    margin: 4px 0 0;
    font-size: 16px;
    font-weight: 500;
    line-height: 26px;
  }
  .offer__code strong {
    font-size: 21px;
    font-weight: 700;
    letter-spacing: 0.5px;
  }
  .script-sale {
    position: absolute;
    left: 400px;
    top: 100px;
    margin: 0;
    font-family: "Great Vibes", cursive;
    font-size: 300px;
    font-weight: 400;
    line-height: 1;
    color: var(--salmon);
    transform: scaleX(0.72);
    transform-origin: left top;
    white-space: nowrap;
  }
  .jewel {
    position: absolute;
  }
  .jewel--pendant {
    left: 808px;
    top: 88px;
    width: 54px;
    height: 128px;
    border-radius: 45% 45% 50% 50%;
    background: radial-gradient(ellipse at 40% 40%, var(--gold-light), var(--gold));
  }
  .jewel--flower-left,
  .jewel--flower-right {
    top: 62px;
    width: 64px;
    height: 66px;
    border-radius: 50%;
    background: radial-gradient(circle at 45% 45%, var(--gem-pink), var(--gem-blue));
  }
  .jewel--flower-left { left: 885px; }
  .jewel--flower-right { left: 958px; }
  .jewel--hoop-left,
  .jewel--hoop-right {
    top: 147px;
    height: 81px;
    border-radius: 20px;
    background: radial-gradient(ellipse at 50% 35%, #f7e36a, #d4a718);
  }
  .jewel--hoop-left { left: 948px; width: 87px; }
  .jewel--hoop-right { left: 1042px; width: 73px; }
  .jewel--bracelet {
    left: 815px;
    top: 232px;
    width: 345px;
    height: 172px;
    border-radius: 50% 50% 0 0 / 55% 55% 0 0;
    background: linear-gradient(180deg, #e9c45a 0%, #d6cfc0 45%, #c99a2c 100%);
  }
</style>
</head>
<body>
<main class="banner">
  <svg class="banner__backdrop" width="1200" height="404" viewBox="0 0 1200 404" aria-hidden="true">
    <defs>
      <linearGradient id="bandGlow" x1="0" y1="0" x2="1" y2="1">
        <stop offset="0" stop-color="#fffaf0" stop-opacity="0.9"/>
        <stop offset="1" stop-color="#fffaf0" stop-opacity="0.2"/>
      </linearGradient>
      <radialGradient id="rightGlow" cx="0.85" cy="0.5" r="0.5">
        <stop offset="0" stop-color="#ffffff"/>
        <stop offset="1" stop-color="#ffffff" stop-opacity="0"/>
      </radialGradient>
    </defs>
    <rect width="1200" height="404" fill="#fbe7bb"/>
    <path d="M0 150 C 250 150, 520 60, 700 0 L 1200 0 L 1200 404 L 560 404 C 420 330, 200 270, 0 270 Z" fill="url(#bandGlow)"/>
    <path d="M0 260 C 180 250, 360 200, 520 120 C 600 80, 660 30, 700 0 L 760 0 C 680 80, 560 190, 360 260 C 230 305, 100 320, 0 330 Z" fill="#fffaf0" opacity="0.7"/>
    <rect width="1200" height="404" fill="url(#rightGlow)"/>
  </svg>

  <h1 class="headline">
    <span class="headline__labor">LABOR</span>
    <span class="headline__day">DAY</span>
  </h1>
  <hr class="headline__rule">

  <div class="offer">
    <p class="offer__savings">Save <strong>15%</strong> on Everything!</p>
    <p class="offer__code">Use Promo Code: <strong>BLOSSOM</strong></p>
  </div>

  <p class="script-sale">Sale</p>

  <div class="jewel jewel--pendant" role="img" aria-label="Gold pendant set with sapphires and rock crystal"></div>
  <div class="jewel jewel--flower-left" role="img" aria-label="Flower earring with pink and blue sapphire petals"></div>
  <div class="jewel jewel--flower-right" role="img" aria-label="Flower earring with pink and blue sapphire petals"></div>
  <div class="jewel jewel--hoop-left" role="img" aria-label="Hammered gold earring"></div>
  <div class="jewel jewel--hoop-right" role="img" aria-label="Hammered gold earring"></div>
  <div class="jewel jewel--bracelet" role="img" aria-label="Twisted gold rope bracelet set with diamonds"></div>
</main>
</body>
</html>
```